Business Card For Construction Company
Falcon Erectors
Business Card For Construction Company - Construction
Creative Brief
Professional
Pavel Lunov
No Address
PavelLunov@FalconErectorsCorp.example
www.FalconErectorsCorp.example

```html
<!DOCTYPE html>
<html lang="en">
<head>
<meta charset="utf-8">
<title>Falcon Erectors Stationery</title>
<link href="https://fonts.googleapis.com/css2?family=Montserrat:wght@400;700;800&display=swap" rel="stylesheet">
<style>
  :root{
    --bg:#e9eaec;
    --paper:#ffffff;
    --blue:#1d5fae;
    --blue-dark:#123f7a;
    --grey:#8d9096;
    --ink:#4a4d52;
    --faint:#eef1f5;
  }
  *{margin:0;padding:0;box-sizing:border-box}
  html,body{width:1200px;height:936px;overflow:hidden;background:var(--bg)}
  body{position:relative;font-family:"Montserrat",Arial,sans-serif;color:var(--ink)}
  .sheet{position:absolute;background:var(--paper);overflow:hidden}
  .swoosh{position:absolute;top:0;right:0}
  .brand{font-weight:800;color:var(--blue);text-transform:uppercase;letter-spacing:.04em;display:flex;align-items:center;white-space:nowrap}
  .brand .mark{display:inline-block;background:var(--blue);margin-right:.4em}

  .letterhead{left:195px;top:68px;width:377px;height:547px}
  .letterhead .brand{position:absolute;left:14px;top:30px;font-size:10px}
  .letterhead .brand .mark{width:9px;height:9px}
  .letterhead .watermark{position:absolute;left:60px;top:195px;width:120px;height:100px;background:var(--faint)}
  .letterhead .contact{position:absolute;left:14px;top:480px;font-size:5.5px;line-height:9px;color:var(--ink)}

  .folder{left:633px;top:43px;width:415px;height:577px}
  .folder .brand{position:absolute;left:0;right:0;top:250px;justify-content:center;font-size:24px}
  .folder .brand .mark{width:22px;height:22px}

  .card-front{left:46px;top:653px;width:177px;height:83px}
  .card-front .brand{position:absolute;left:8px;top:10px;font-size:7px}
  .card-front .brand .mark{width:7px;height:7px}
  .card-front .contact{position:absolute;left:8px;top:40px;font-size:4.5px;line-height:7px}
  .card-front .name{position:absolute;right:12px;bottom:8px;font-size:5px;font-weight:700;color:var(--ink)}

  .card-back{left:46px;top:762px;width:177px;height:93px}
  .card-back .brand{position:absolute;left:0;right:0;top:38px;justify-content:center;font-size:13px}
  .card-back .brand .mark{width:12px;height:12px}

  .envelope-front{left:268px;top:673px;width:430px;height:200px}
  .envelope-front .brand{position:absolute;left:12px;top:20px;font-size:9px}
  .envelope-front .brand .mark{width:8px;height:8px}

  .envelope-back{left:739px;top:673px;width:425px;height:200px}
  .envelope-back .flap{position:absolute;left:0;top:0}
  .envelope-back .web{position:absolute;left:0;right:0;top:22px;text-align:center;color:#fff;font-size:8px;letter-spacing:.3em;text-transform:uppercase}
</style>
</head>
<body>

<section class="sheet letterhead">
  <svg class="swoosh" width="150" height="150" viewBox="0 0 150 150">
    <path d="M0 0 H150 V150 C145 70 90 14 0 0Z" fill="var(--grey)"/>
    <path d="M10 0 H150 V138 C140 66 92 16 10 0Z" fill="var(--blue)"/>
  </svg>
  <div class="brand"><span class="mark"></span>Falcon Erectors</div>
  <div class="watermark"></div>
  <div class="contact">
    <div>T 555 010 2040</div>
    <div>F 555 010 2041</div>
    <div>PavelLunov@FalconErectorsCorp.example</div>
    <div>www.FalconErectorsCorp.example</div>
  </div>
</section>

<section class="sheet folder">
  <svg class="swoosh" width="200" height="170" viewBox="0 0 200 170">
    <path d="M0 0 H200 V170 C190 80 120 14 0 0Z" fill="var(--grey)"/>
    <path d="M14 0 H200 V156 C186 76 124 18 14 0Z" fill="var(--blue)"/>
  </svg>
  <div class="brand"><span class="mark"></span>Falcon Erectors</div>
</section>

<section class="sheet card-front">
  <svg class="swoosh" width="70" height="50" viewBox="0 0 70 50">
    <path d="M0 0 H70 V50 C66 22 40 4 0 0Z" fill="var(--grey)"/>
    <path d="M6 0 H70 V45 C64 20 42 5 6 0Z" fill="var(--blue)"/>
  </svg>
  <div class="brand"><span class="mark"></span>Falcon Erectors</div>
  <div class="contact">
    <div>Project Director</div>
    <div>555 010 2040</div>
    <div>PavelLunov@FalconErectorsCorp.example</div>
  </div>
  <div class="name">Pavel Lunov</div>
</section>

<section class="sheet card-back">
  <div class="brand"><span class="mark"></span>Falcon Erectors</div>
</section>

<section class="sheet envelope-front">
  <svg class="swoosh" width="170" height="95" viewBox="0 0 170 95">
    <path d="M0 0 H170 V95 C160 40 100 8 0 0Z" fill="var(--grey)"/>
    <path d="M12 0 H170 V86 C158 38 104 10 12 0Z" fill="var(--blue)"/>
  </svg>
  <div class="brand"><span class="mark"></span>Falcon Erectors</div>
</section>

<section class="sheet envelope-back">
  <svg class="flap" width="425" height="200" viewBox="0 0 425 200">
    <path d="M0 0 H425 V140 C360 60 200 70 0 70Z" fill="var(--grey)"/>
    <path d="M0 0 H425 V128 C360 54 200 62 0 62Z" fill="var(--blue)"/>
  </svg>
  <div class="web">www.FalconErectorsCorp.example</div>
</section>

</body>
</html>
```